Regional and National Rugby Training and Player Development Company

We need a new responsive website design that is easy to navigate and encourages people to register for our programs.

Registration and payment could be written into the site but it can also be externally integrated as it is currently.

I want clean lines, bright images, and a webpage that is easy to update and manage. Currently using WordPress.
Updates

Ferncrest Rugby runs four programs:  Junior Sunfield Rugby Clinics, Frostline Court Tag Rugby, Bloomtide Skills Clinics, and the "Athlete Growth Pathway" otherwise known as the Forge

Ultimately, Ferncrest Rugby wants to attract the top players across the province of Ontario to join our corner-stone program, the Frostline Forge.

We have had many players play at the provincial level and a select handful go on to represent Canada.  We aspire to set the standard for off-season junior rugby player development.

Reason: 1) Laptop crashed on Thurs. which meant I couldn't make a fair decision this weekend. 2). There are FIVE very good designs, each somewhat unique. I want to see what designers come up with when I outline what I like in each as a requirement of what has been provided. Thank you for your understanding and efforts in this regard. Sincerely, MB Sent from my iPad

Thank you for all your efforts and patience in this design campaign, I truly appreciate it.  Apologies for the lack of communication but as a full-time high school teacher, sometimes my "real job" gets put to the side.  

I have reduced over 30 designs to five... you are the five remaining I hope to take certain aspects of each that I like best and provide some feedback to you the designers, in order to make final adjustments before my final decision.

I hope you find this process agreeable and again, thank you for your patience and efforts in this campaign.  I think each of your designs look fantastic and are a drastic and valuable improvement of what I have been using up to this point.

Appreciatively,

MB

Voting poll results are in and there are three distinct leaders... going to focus on these three this week and come to a final decision before Friday.

Each designer will be contacted privately to provide some feedback and see what the best final product can look like.

Thank you for your patience and high-quality work!

MB

Reason: Just too much going on at the moment and trying to stay on top of this. Apologies to all. Just had the results of the voting poll come in and have reduced choices to two clear leaders with a third alternate. Going to provide feedback for all three today and hope to make final decision by Friday. Thank you for your efforts.

Target Market(s)

Junior rugby players (boys and girls) between the ages of 12 and 20... more importantly, their parents!

Requirements
Must have
• Must have high-resolution, clean lines, and encourage registration in programs. I would like it to be integrated with my YouTube page as well as other social media.

```html
<!DOCTYPE html>
<html lang="en">
<head>
<meta charset="utf-8">
<title>Ferncrest Rugby Canada</title>
<link rel="stylesheet" href="https://fonts.googleapis.com/css2?family=Roboto+Condensed:wght@400;700&family=Open+Sans:wght@400;600;700&family=Cardo:ital@0;1&display=swap">
<style>
:root{
  --red:#e1232b;
  --red-dark:#b3161d;
  --ink:#1d1d1d;
  --header:#2a2a2a;
  --footer:#1f1f1f;
  --band:#ebebeb;
  --text:#555;
  --muted:#8a8a8a;
  --gold:#f4c21a;
  --white:#fff;
}
*{box-sizing:border-box;margin:0;padding:0}
html,body{width:1200px;height:2349px;overflow:hidden}
body{position:relative;background:var(--white);font-family:"Open Sans",Arial,sans-serif;color:var(--text)}
.abs{position:absolute}
.cond{font-family:"Roboto Condensed","Arial Narrow",sans-serif}

/* header */
.site-header{left:0;top:0;width:1200px;height:100px;background:linear-gradient(#333,#222)}
.brand{left:140px;top:22px;display:flex;align-items:center;gap:10px}
.brand-dot{width:40px;height:40px;border-radius:50%;background:var(--red)}
.brand-name{font-family:"Roboto Condensed",sans-serif;font-weight:700;font-size:19px;line-height:21px;color:var(--red);width:140px}
.utility{left:450px;top:14px;display:flex;align-items:center;gap:10px}
.utility svg{display:block}
.search{width:180px;height:26px;background:#1a1a1a;border:1px solid #444;border-radius:2px;color:#888;font-size:12px;padding:5px 8px;position:relative}
.search svg{position:absolute;right:6px;top:6px}
.social{display:flex;gap:8px;margin-left:14px}
.social span{width:26px;height:26px;border-radius:50%;background:#8b8b8b;display:block}
.main-nav{left:450px;top:70px;display:flex;gap:32px;font-family:"Roboto Condensed",sans-serif;font-weight:700;font-size:15px;color:var(--white)}
.account{left:842px;top:0;height:100px;display:flex}
.account .register{width:110px;background:#2f2f2f;color:#fff}
.account .login{width:106px;background:var(--red);color:#fff}
.account div{display:flex;flex-direction:column;align-items:center;justify-content:flex-end;padding-bottom:14px;gap:8px;font-family:"Roboto Condensed",sans-serif;font-weight:700;font-size:15px}
.or{left:942px;top:50px;width:22px;height:22px;border-radius:50%;background:#222;border:2px solid var(--red);color:#fff;font-size:10px;font-weight:700;text-align:center;line-height:18px}

/* hero */
.hero{left:0;top:100px;width:1200px;height:555px;background:linear-gradient(180deg,#6b8a4c 0%,#3d5a2a 55%,#2e4a1f 100%)}
.hero-players{left:100px;top:100px;width:440px;height:555px;background:linear-gradient(180deg,#a9a29a,#7d6d62 60%,#5d5a4f)}
.hero-quote{left:515px;top:228px;width:540px;text-align:right;font-family:"Cardo",Georgia,serif;color:#fff;font-size:66px;line-height:64px;text-shadow:0 2px 6px rgba(0,0,0,.5)}
.hero-text{left:555px;top:450px;width:505px;font-family:"Cardo",Georgia,serif;color:#fff;font-size:23px;line-height:31px;text-shadow:0 1px 4px rgba(0,0,0,.6)}

/* intro */
.intro{left:0;top:655px;width:1200px;height:437px;background:linear-gradient(#fafafa,#fff)}
.video{left:140px;top:745px;width:435px;height:245px;background:#0b0b0b;border:6px solid #e6e6e6;box-shadow:0 4px 12px rgba(0,0,0,.3)}
.video .play{position:absolute;left:160px;top:70px}
.video .bar{position:absolute;left:10px;bottom:10px;right:10px;height:28px;background:#1a1a1a;display:flex;align-items:center;gap:10px;padding:0 8px}
.video .track{flex:1;height:6px;background:#555;position:relative}
.video .track i{position:absolute;left:0;top:0;height:6px;width:32%;background:#4aa7d9}
.video .side{position:absolute;right:8px;top:8px;display:flex;flex-direction:column;gap:6px}
.video .side span{width:22px;height:22px;background:#222;display:block}
.tabs{left:662px;top:745px;display:flex;font-family:"Roboto Condensed",sans-serif;font-size:16px}
.tabs span{padding:10px 14px;color:var(--muted)}
.tabs .active{color:var(--red);font-weight:700;background:#fff;border:1px solid #ddd;border-bottom:none}
.tab-panel{left:662px;top:792px;width:392px;height:198px;background:#fff;border:1px solid #ddd;box-shadow:0 2px 6px rgba(0,0,0,.08)}
.tab-panel .mark{position:absolute;left:20px;top:50px}
.tab-panel p{position:absolute;left:110px;top:26px;width:270px;font-size:13px;line-height:20px;color:#666}
.tab-panel a{color:var(--red);text-decoration:none}

/* programs */
.programs{left:0;top:1092px;width:1200px;height:548px;background:var(--band)}
.programs-title{left:362px;top:1075px;width:476px;height:80px;background:#fff;box-shadow:0 2px 6px rgba(0,0,0,.12);text-align:center;font-family:"Roboto Condensed",sans-serif;font-size:32px;line-height:80px;color:var(--ink);font-weight:700}
.programs-title em{font-style:normal;color:var(--red);font-weight:400}
.programs-title b{font-weight:700}
.program{top:1175px;width:280px;text-align:center}
.program h3{font-family:"Roboto Condensed",sans-serif;font-weight:400;font-size:23px;line-height:27px;color:var(--red)}
.program h3 span{display:block;color:var(--ink)}
.program .photo{width:160px;height:160px;border-radius:50%;margin:22px auto 0;border:6px solid #fff;box-shadow:0 0 0 1px #ccc}
.program p{margin:28px auto 0;width:255px;font-size:13.5px;line-height:22px;color:#555}
.program .more{display:inline-block;margin-top:26px;background:var(--red);color:#fff;font-size:12px;padding:4px 10px}
.p1{left:155px}.p2{left:460px}.p3{left:763px}
.arrow{top:1310px}

/* news & testimonials */
.news{left:140px;top:1675px;width:460px}
.section-head{font-family:"Roboto Condensed",sans-serif;font-weight:700;font-size:24px;color:var(--ink);display:flex;align-items:center;gap:10px}
.section-head i{width:28px;height:28px;background:#aab;display:block}
.news-item{display:flex;gap:18px;margin-top:30px}
.news-item .thumb{width:52px;height:52px;background:linear-gradient(135deg,#3e69c4,#c6d6ee);flex:none}
.news-item h4{font-size:14px;font-weight:700;color:var(--ink)}
.news-item p{font-size:13px;line-height:18px;color:#555}
.news-item a{color:var(--red);text-decoration:none}
.testimonials{left:628px;top:1675px;width:430px}
.quote-wrap{display:flex;gap:14px;margin-top:20px}
.portrait{width:98px;height:100px;background:linear-gradient(#a6a39a,#5e5a53);flex:none}
.quote{background:#f3f3f3;border:1px dashed #ccc;padding:14px 16px;font-family:"Cardo",Georgia,serif;font-style:italic;font-size:14px;line-height:20px;color:#444}
.cite{margin-top:12px;text-align:center;font-family:"Cardo",Georgia,serif;font-style:italic;font-size:14px;color:var(--red)}
.register-cta{left:478px;top:1977px;width:244px;height:52px;background:linear-gradient(var(--red),var(--red-dark));border-radius:4px;color:#fff;font-family:"Roboto Condensed",sans-serif;font-size:26px;display:flex;align-items:center;justify-content:center;gap:12px;box-shadow:0 3px 6px rgba(0,0,0,.25)}

/* footer */
.site-footer{left:0;top:2060px;width:1200px;height:289px;background:var(--footer)}
.footer-brand{left:140px;top:2085px;font-family:"Roboto Condensed",sans-serif;font-weight:700;font-size:19px;color:var(--gold)}
.contact{left:140px;top:2125px;font-size:13px;color:#bbb;line-height:20px}
.contact div{display:flex;align-items:center;gap:12px;margin-bottom:16px}
.follow{left:140px;top:2235px;display:flex;align-items:center;gap:6px;color:#fff;font-weight:700;font-size:15px}
.follow span{width:24px;height:24px;background:#5a6fa5;display:block}
.map{left:430px;top:2142px;width:627px;height:146px;background:linear-gradient(135deg,#e8e3d6,#d7dccb);border:6px solid #3a3a3a}
.copyright{left:0;top:2308px;width:1200px;height:41px;background:#161616;color:#999;font-size:13px;text-align:center;line-height:41px}
</style>
</head>
<body>

<header class="abs site-header"></header>
<div class="abs brand"><span class="brand-dot"></span><span class="brand-name">Ferncrest Rugby Canada</span></div>
<div class="abs utility">
  <svg width="18" height="18" viewBox="0 0 18 18"><path d="M2 9 9 3l7 6M4 8v8h10V8" fill="none" stroke="#999" stroke-width="1.6"/></svg>
  <svg width="20" height="14" viewBox="0 0 20 14"><rect x="1" y="1" width="18" height="12" fill="none" stroke="#999" stroke-width="1.6"/><path d="M1 1l9 7 9-7" fill="none" stroke="#999" stroke-width="1.6"/></svg>
  <div class="search">Search here<svg width="14" height="14" viewBox="0 0 14 14"><circle cx="8" cy="6" r="4" fill="none" stroke="#999" stroke-width="1.6"/><path d="M5 9 1 13" stroke="#999" stroke-width="1.8"/></svg></div>
  <div class="social"><span></span><span></span><span></span></div>
</div>
<nav class="abs main-nav"><span>PLAYER DEVELOPMENT</span><span>COMMUNITY</span><span>FRC NEWS</span></nav>
<div class="abs account">
  <div class="register"><svg width="30" height="30" viewBox="0 0 30 30"><circle cx="15" cy="9" r="7" fill="#fff"/><path d="M2 30c0-9 6-13 13-13s13 4 13 13z" fill="#fff"/></svg>REGISTER</div>
  <div class="login"><svg width="26" height="30" viewBox="0 0 26 30"><path d="M6 13V9a7 7 0 0 1 14 0v4" fill="none" stroke="#fff" stroke-width="3"/><rect x="2" y="13" width="22" height="16" rx="2" fill="#fff"/></svg>LOGIN IN</div>
</div>
<div class="abs or">OR</div>

<section class="abs hero" role="img" aria-label="Rugby players standing on a training field with a team playing behind them"></section>
<div class="abs hero-players" role="img" aria-label="Two rugby players in kit, one holding a ball"></div>
<h1 class="abs hero-quote">“We Make<br>&nbsp;Good Players<br>Great!”</h1>
<p class="abs hero-text">"The team atmosphere is great. From catching the ball, to showing up everyweek, when you don't, you're missed - it's a close-knit group, like afamily, like any great rugby team..."</p>

<section class="abs intro"></section>
<div class="abs video">
  <svg class="play" width="90" height="90" viewBox="0 0 90 90"><circle cx="45" cy="45" r="41" fill="none" stroke="#fff" stroke-width="4"/><path d="M36 28l26 17-26 17z" fill="#fff"/></svg>
  <div class="side"><span></span><span></span><span></span><span></span></div>
  <div class="bar"><svg width="14" height="14" viewBox="0 0 14 14"><path d="M2 1l11 6-11 6z" fill="#fff"/></svg><div class="track"><i></i></div><span style="color:#4aa7d9;font-size:11px;font-weight:700">HD</span></div>
</div>
<div class="abs tabs"><span class="active">MISSION</span><span>VISION</span><span>LEARNING CONTINUUM</span></div>
<div class="abs tab-panel">
  <svg class="mark" width="70" height="70" viewBox="0 0 70 70"><circle cx="35" cy="35" r="32" fill="#f3d7a6"/><circle cx="35" cy="35" r="24" fill="#fff" stroke="var(--red)" stroke-width="5"/><rect x="31" y="20" width="8" height="20" fill="var(--red)"/><rect x="31" y="44" width="8" height="7" fill="var(--red)"/></svg>
  <p>Ferncrest Rugby Canada is about making skilled, informed, and knowledgeable players. Our mission is to develop young players within an environment that is challenging, yet rewarding in order to see them attain their goals in the sport of rugby...<a href="#">Read More</a></p>
</div>

<section class="abs programs"></section>
<div class="abs programs-title"><em>RUGBY RUNS</em> <b>FOUR PROGRAMS</b></div>
<svg class="abs arrow" style="left:138px" width="30" height="60" viewBox="0 0 30 60"><path d="M28 2 2 30l26 28" fill="none" stroke="#bbb" stroke-width="2"/></svg>
<svg class="abs arrow" style="left:1032px" width="30" height="60" viewBox="0 0 30 60"><path d="M2 2l26 28L2 58" fill="none" stroke="#bbb" stroke-width="2"/></svg>
<article class="abs program p1">
  <h3>Junior Sunfield<span>Rugby Clinics</span></h3>
  <div class="photo" role="img" aria-label="Players in a summer scrum" style="background:linear-gradient(#7e9a5e,#3d5b8c)"></div>
  <p>Our summer clinics are a great way reinforce current skill sets for young players with some experience or provide a fun learning opportunity for those that are new to the game.</p>
  <span class="more">Read More →</span>
</article>
<article class="abs program p2">
  <h3>Frostline Court<span>Tag Rugby</span></h3>
  <div class="photo" role="img" aria-label="Player in a hooped jersey holding a ball" style="background:linear-gradient(#c9c2b5,#a03a3a)"></div>
  <p>Our co-ed indoor tag rugby leagues are a fun and enjoyable way to keep fit in the winter months while working on some one's skills in preparation for spring/summer.</p>
  <span class="more">Read More →</span>
</article>
<article class="abs program p3">
  <h3>Bloomtide Skills<span>Clinics</span></h3>
  <div class="photo" role="img" aria-label="Players running with the ball in spring training" style="background:linear-gradient(#8fb0d0,#6d8f4a)"></div>
  <p>Lorem Ipsum is simply dummy text of the printing and typesetting industry. Lorem Ipsum has been the industry's standard dummy text when unknown ever since the 1500s,</p>
  <span class="more">Read More →</span>
</article>

<section class="abs news">
  <h2 class="section-head"><i></i>LATEST NEWS EVENT</h2>
  <div class="news-item"><span class="thumb" role="img" aria-label="News thumbnail"></span><div><h4>The standard Lorem Ipsum passage</h4><p>Lorem ipsum dolor sit amet, consectetur adipisicing elit, sed do eiusmod tempor incididunt ut labore. <a href="#">[Read</a></p></div></div>
  <div class="news-item"><span class="thumb" role="img" aria-label="News thumbnail"></span><div><h4>The standard Lorem Ipsum passage</h4><p>Lorem ipsum dolor sit amet, consectetur adipisicing elit, sed do eiusmod tempor incididunt ut labore. <a href="#">[Read</a></p></div></div>
  <div class="news-item"><span class="thumb" role="img" aria-label="News thumbnail"></span><div><h4>The standard Lorem Ipsum passage</h4><p>Lorem ipsum dolor sit amet, consectetur adipisicing elit, sed do eiusmod tempor incididunt ut labore. <a href="#">[Read More...]</a></p></div></div>
</section>

<section class="abs testimonials">
  <h2 class="section-head"><i style="background:#8fa8cf"></i>TESTIMONIALS</h2>
  <div class="quote-wrap">
    <div class="portrait" role="img" aria-label="Portrait of the testimonial author"></div>
    <div>
      <p class="quote">"Personally, I see so much benefit to the program you run; there is a definite need for this level of training in our [rugby] community and others. I can't believe the progress that the athletes made and their overall desire to improve for the love of the game.I learned a lot for sure and definitely want to be involved again!"</p>
      <p class="cite">- CEO, Halvard Capital Partners, Geneva</p>
    </div>
  </div>
</section>

<a class="abs register-cta"><svg width="26" height="28" viewBox="0 0 26 28"><rect x="1" y="3" width="18" height="23" fill="#fff"/><path d="M10 20l12-14 3 3-12 14-4 1z" fill="#fff" stroke="var(--red)" stroke-width="1.5"/></svg>REGISTER NOW</a>

<footer class="abs site-footer"></footer>
<div class="abs footer-brand">Ferncrest Rugby Canada</div>
<div class="abs contact">
  <div><svg width="12" height="16" viewBox="0 0 12 16"><path d="M6 16S0 9 0 6a6 6 0 0 1 12 0c0 3-6 10-6 10z" fill="#888"/><circle cx="6" cy="6" r="2" fill="#1f1f1f"/></svg>48 Alderbrook Lane Westvale, K2P 4R9</div>
  <div><svg width="14" height="14" viewBox="0 0 14 14"><path d="M3 0l3 3-2 2c1 2 3 4 5 5l2-2 3 3-2 3C6 14 0 8 0 2z" fill="#888"/></svg>Ph. (555) 014-3872</div>
  <div><svg width="16" height="12" viewBox="0 0 16 12"><rect width="16" height="12" fill="#888"/><path d="M0 0l8 6 8-6" fill="none" stroke="#1f1f1f" stroke-width="1.4"/></svg>hello@ferncrestrugby.example</div>
</div>
<div class="abs follow">Follow Us : <span></span><span></span><span></span><span style="background:#a33"></span></div>
<div class="abs map" role="img" aria-label="Street map showing the club location"></div>
<div class="abs copyright">Copyright © 2013 Ferncrest Rugby Canada. All Rights Reserved.</div>

</body>
</html>
```